Business card for Chiropractic clinics needs reworked / redesigned

The business card in attachment was designed 10 years ago. It is in need of an update.
We have 2 clinics:
VELDHOVE KLINIEK & VELDHOVE KLINIEK NOORD
Only one address needs to be on the card for doctors that only work in one clinic and two addresses need to be on the card for the doctors that work in both clinics.

Target Market(s)

patients/referrers

Industry/Entity Type

Medical

Contact Information for Business Card

Logo (in full or zoomed-in)
Clinic Name
Doctor name and title
clinic address, website, tel, email

Font styles to use
Sans Serif

Colors

Designer to choose colors to be used in the design.

Requirements
Must have
• Good contrast/readability
• We like modern minimalistic designs
• The Bcard needs to project our very high standard of proficiency/professionalism
Should not have
• Not curly
• Not to much colours

```html
<!DOCTYPE html>
<html lang="nl">
<head>
<meta charset="utf-8">
<title>Veldhove Kliniek – visitekaartjes</title>
<link rel="stylesheet" href="https://fonts.googleapis.com/css2?family=Barlow:wght@300;400;500;600&display=swap">
<style>
  :root {
    --backdrop: #dcdddf;
    --card-light: #ffffff;
    --card-dark: #012124;
    --ink: #012124;
    --accent: #4f8a75;
  }
  * { margin: 0; padding: 0; box-sizing: border-box; }
  html, body {
    width: 1200px; height: 655px; overflow: hidden;
    background: var(--backdrop);
    font-family: "Barlow", Arial, sans-serif;
    color: var(--ink);
  }
  .card {
    position: absolute; top: 80px;
    width: 320px; height: 496px;
    border-radius: 14px;
    background: var(--card-light);
    box-shadow: 0 3px 12px rgba(0,0,0,0.12);
    overflow: hidden;
  }
  .card--front { left: 80px; }
  .card--logo-light { left: 440px; }
  .card--logo-dark { left: 800px; background: var(--card-dark); }

  .doctor {
    position: absolute; right: 20px; top: 52px;
    text-align: right;
  }
  .doctor__name {
    font-weight: 400; font-size: 32px; line-height: 35px;
    letter-spacing: 0.2px;
  }
  .doctor__title {
    margin-top: 5px;
    font-weight: 400; font-size: 13px; letter-spacing: 0.3px;
  }

  .clinic {
    position: absolute; left: 122px;
  }
  .clinic--main { top: 271px; }
  .clinic--north { top: 381px; }
  .clinic__name {
    font-weight: 600; font-size: 14px; line-height: 18px;
    margin-bottom: 2px; white-space: nowrap;
  }
  .clinic__line {
    display: flex; align-items: center; gap: 7px;
    font-weight: 400; font-size: 14px; line-height: 18px;
    white-space: nowrap;
  }
  .clinic__line svg { width: 11px; height: 11px; flex: none; fill: var(--accent); }

  .brand {
    position: absolute; inset: 0;
    display: flex; align-items: center; justify-content: center; gap: 10px;
    font-weight: 500; font-size: 24px; letter-spacing: 0.5px;
  }
  .brand__dot { width: 12px; height: 12px; border-radius: 50%; background: currentColor; }
  .card--logo-light .brand { color: var(--ink); }
  .card--logo-dark .brand { color: #ffffff; }
</style>
</head>
<body>
<svg width="0" height="0" style="position:absolute" aria-hidden="true">
  <symbol id="icon-pin" viewBox="0 0 12 12"><path d="M6 0.5a4 4 0 0 0-4 4c0 3 4 7 4 7s4-4 4-7a4 4 0 0 0-4-4zm0 5.6a1.6 1.6 0 1 1 0-3.2 1.6 1.6 0 0 1 0 3.2z"/></symbol>
  <symbol id="icon-phone" viewBox="0 0 12 12"><path d="M2.6 0.8l1.8 0 .8 2.6-1.2 1a7 7 0 0 0 3.4 3.4l1-1.2 2.6.8v1.8c0 .6-.5 1-1 1A10 10 0 0 1 1.6 1.8c0-.5.4-1 1-1z"/></symbol>
  <symbol id="icon-mail" viewBox="0 0 12 12"><path d="M0.5 2.5h11v7h-11z M1 3l5 3.8L11 3" /><path d="M0.5 2.5L6 6.6l5.5-4.1v7h-11z" fill="none"/></symbol>
  <symbol id="icon-globe" viewBox="0 0 12 12"><path d="M6 0.5a5.5 5.5 0 1 0 0 11 5.5 5.5 0 0 0 0-11zm-1 1.3C4.4 2.8 4 4 3.9 5.3H1.8A4.3 4.3 0 0 1 5 1.8zm2 0a4.3 4.3 0 0 1 3.2 3.5H8.1C8 4 7.6 2.8 7 1.8zM5.1 5.3c.1-1.4.5-2.6.9-3.4.4.8.8 2 .9 3.4zm-3.3 1.4h2.1c.1 1.3.5 2.5 1.1 3.5a4.3 4.3 0 0 1-3.2-3.5zm3.3 0h1.8c-.1 1.4-.5 2.6-.9 3.4-.4-.8-.8-2-.9-3.4zm3 0h2.1A4.3 4.3 0 0 1 7 10.2c.6-1 1-2.2 1.1-3.5z"/></symbol>
</svg>

<section class="card card--front" aria-label="Voorzijde visitekaartje">
  <header class="doctor">
    <h1 class="doctor__name">Pieter<br>Vanlaere D.C.</h1>
    <p class="doctor__title">CHIROPRACTOR</p>
  </header>

  <address class="clinic clinic--main" style="font-style:normal">
    <p class="clinic__name">VELDHOVE KLINIEK</p>
    <p class="clinic__line"><svg><use href="#icon-pin"/></svg>Lindenstraat 48</p>
    <p class="clinic__line"><svg><use href="#icon-phone"/></svg>09 210 45 87</p>
    <p class="clinic__line"><svg><use href="#icon-mail"/></svg>info@veldhovekliniek.be</p>
    <p class="clinic__line"><svg><use href="#icon-globe"/></svg>veldhovekliniek.be</p>
  </address>

  <address class="clinic clinic--north" style="font-style:normal">
    <p class="clinic__name">VELDHOVE KLINIEK NOORD</p>
    <p class="clinic__line"><svg><use href="#icon-pin"/></svg>Kerkplein 17</p>
    <p class="clinic__line"><svg><use href="#icon-phone"/></svg>09 380 62 19</p>
    <p class="clinic__line"><svg><use href="#icon-mail"/></svg>info@veldhovenoord.be</p>
    <p class="clinic__line"><svg><use href="#icon-globe"/></svg>veldhovenoord.be</p>
  </address>
</section>

<section class="card card--logo-light" aria-label="Achterzijde licht">
  <div class="brand"><span class="brand__dot"></span>Veldhove Kliniek</div>
</section>

<section class="card card--logo-dark" aria-label="Achterzijde donker">
  <div class="brand"><span class="brand__dot"></span>Veldhove Kliniek</div>
</section>
</body>
</html>
```